Web site for fans of TV series "The Drifter Pass"

1. Description: This is a new web site for the fans of a Western TV series called "The Drifter Pass". It ran for nine seasons from 1962 to 1971.

It is going to be a fan-generated content. The site will use a proprietary social-sharing software in the back-end. The software could be looked as your personal Chatterbox service running on your own domain. In fact, anyone can use this software for any social-sharing need.

A sample of the software running a social-sharing site:
http://www.valtemo.com

The public-facing software has ten sections or modules as follows:

1. Survey
2. Blog
3. Links
4. Video
5. Music
6. Photo
7. Cartoon
8. Photo Album
9. Quotes
10. Follow/Followers (like squawkr)

2. Delivery. Three designs for three pages. I need delivery in PSD, JPG and AI formats..

3. Pages

3.1. Homepage
Example: http://www.valtemo.com

IMPORTANT REQUIREMENT. The Homepage should be designed such that I or the site Admin with basic knowledge of HTML and CSS can move around different sections or modules without a need to rewrite the CSS or HTML code.

3.2. Point of Entry or Summary page.
Example: http://valtemo.com/vksp/blog/latest/

3.3. Detail page
Example: http://valtemo.com/vksp/blog/2929/

Project Deadline Extended
Reason: I received acceptable designs late. I would like to give this contest 7 more days. This gives me time to work with current designs and just in case I receive new designs.

Target Market(s)

Age: Above 40, average age is 50-55

Gender: Primarily female

Location: Primarily United States, but we have a visible following in Europe and South America.

Industry/Entity Type

Tv

Requirements
Must have
• 1. The image/icon of The Drifter Pass. You can capture it via ClipHollow clips at the opening of the show.

2. Red color (burgundy. See shirt of the main character called Drifter played by actor Walter Penhale.

3. The American West spirit (yes, you may call it the cowboy spirit)

4. The Homepage should be designed such that a person with basic knowledge of CSS and HTML coding can move around different sections or modules.
Should not have
• No cartoonish icons.

```html
<!DOCTYPE html>
<html lang="en">
<head>
<meta charset="utf-8">
<title>The Drifter Pass — Footer</title>
<link href="https://fonts.googleapis.com/css2?family=Lato:wght@400;700&display=swap" rel="stylesheet">
<style>
  :root {
    --burgundy: #ab1e22;
    --rule-top: #d9bc8f;
    --rule-divider: #5e1416;
    --ink: #ffffff;
    --field-border: #cccccc;
    --field-placeholder: #9a9a9a;
    --teal: #1abc9c;
    --teal-border: #17a98c;
    --ic-orange: #e8771e;
    --ic-green: #7cb82f;
    --ic-pink: #e9436f;
    --ic-red: #d62a2a;
    --ic-grey: #444444;
    --ic-blue: #2d7fd3;
  }
  * { box-sizing: border-box; margin: 0; padding: 0; }
  html, body { width: 1200px; height: 532px; overflow: hidden; }
  body {
    background: var(--burgundy);
    font-family: "Lato", Arial, sans-serif;
    color: var(--ink);
    position: relative;
  }
  .site-footer { position: absolute; inset: 0; border-top: 3px solid var(--rule-top); }
  .col { position: absolute; top: 0; }
  .col-heading {
    position: absolute;
    font-weight: 400;
    font-size: 26px;
    line-height: 1;
    white-space: nowrap;
    display: flex;
    align-items: center;
    gap: 8px;
  }
  .col-heading svg { width: 22px; height: 22px; fill: var(--ink); }
  .link-list { list-style: none; position: absolute; }
  .link-list li {
    height: 35.7px;
    display: flex;
    align-items: center;
    font-weight: 700;
    font-size: 17px;
    white-space: nowrap;
  }
  .mod-icon {
    width: 19px; height: 19px; margin-right: 10px; flex: none;
    display: inline-flex; align-items: center; justify-content: center;
  }
  .mod-icon svg { width: 13px; height: 13px; fill: var(--ink); }

  .col-content { left: 40px; }
  .col-content .col-heading { top: 34px; left: 0; }
  .col-content .link-list { top: 69px; left: 30px; }

  .col-about { left: 231px; }
  .col-about .col-heading { top: 34px; left: 0; }
  .col-about .link-list { top: 75px; left: 29px; }

  .col-support { left: 422px; }
  .col-support .col-heading.support { top: 34px; left: 0; }
  .col-support .link-list.support-list { top: 75px; left: 30px; }
  .col-support .col-heading.legal { top: 163px; left: 0; }
  .col-support .link-list.legal-list { top: 202px; left: 30px; }

  .col-contact { left: 613px; }
  .col-contact .col-heading { top: 35px; left: 0; }
  .social-row {
    position: absolute; left: 28px;
    display: flex; align-items: center; gap: 20px;
    font-size: 16px; font-weight: 700; white-space: nowrap;
  }
  .social-row.first { top: 136px; }
  .social-row.second { top: 241px; }
  .mail-icon { width: 32px; height: 24px; fill: none; stroke: var(--ink); stroke-width: 2.2; }
  .phone {
    position: absolute; left: 28px; top: 341px;
    display: flex; align-items: center; gap: 4px;
    font-size: 17px;
  }
  .phone svg { width: 22px; height: 24px; fill: var(--ink); }

  .col-newsletter { left: 899px; }
  .newsletter-heading {
    position: absolute; top: 32px; left: 0;
    font-size: 24px; font-weight: 400; white-space: nowrap;
  }
  .email-field {
    position: absolute; top: 67px; left: 0;
    width: 262px; height: 36px;
    background: #fff; border: 1px solid var(--field-border); border-radius: 3px;
    padding: 0 9px; font-family: Arial, sans-serif; font-size: 16px;
    color: var(--field-placeholder); display: flex; align-items: center;
  }
  .subscribe-btn {
    position: absolute; top: 113px; left: 0;
    width: 107px; height: 43px;
    background: var(--teal); border: 1px solid var(--teal-border); border-radius: 4px;
    color: #fff; font-family: Arial, sans-serif; font-size: 17px;
    display: flex; align-items: center; justify-content: center;
  }

  .footer-divider {
    position: absolute; top: 456px; left: 0; width: 100%;
    border-top: 1px solid var(--rule-divider);
  }
  .copyright {
    position: absolute; top: 483px; left: 40px;
    font-size: 17px; white-space: nowrap;
  }
</style>
</head>
<body>
<footer class="site-footer">

  <section class="col col-content">
    <h3 class="col-heading">
      <svg viewBox="0 0 24 24"><path d="M12 1.5l3.2 7 7.6.8-5.7 5.1 1.6 7.5L12 18l-6.7 3.9 1.6-7.5L1.2 9.3l7.6-.8z"/></svg>
      Content
    </h3>
    <ul class="link-list">
      <li><span class="mod-icon" style="background:var(--ic-blue)"><svg viewBox="0 0 12 12"><path d="M5 1h2v4h4v2H7v4H5V7H1V5h4z"/></svg></span>Latest</li>
      <li><span class="mod-icon" style="background:var(--ic-green)"><svg viewBox="0 0 12 12"><rect x="1" y="6" width="2" height="5"/><rect x="5" y="3" width="2" height="8"/><rect x="9" y="8" width="2" height="3"/></svg></span>Survey</li>
      <li><span class="mod-icon" style="background:var(--ic-pink)"><svg viewBox="0 0 12 12"><rect x="1" y="2" width="10" height="1.5"/><rect x="1" y="5" width="10" height="1.5"/><rect x="1" y="8" width="10" height="1.5"/></svg></span>Blog</li>
      <li><span class="mod-icon" style="background:var(--ic-orange)"><svg viewBox="0 0 12 12"><path d="M5 1h5v2H7v6a2 2 0 1 1-2-2z"/></svg></span>Music</li>
      <li><span class="mod-icon" style="background:var(--ic-blue)"><svg viewBox="0 0 12 12"><path d="M5 1h2v4h4v2H7v4H5V7H1V5h4z"/></svg></span>Photo</li>
      <li><span class="mod-icon" style="background:var(--ic-red)"><svg viewBox="0 0 12 12"><path d="M3 2l7 4-7 4z"/></svg></span>Video</li>
      <li><span class="mod-icon" style="background:var(--ic-grey)"><svg viewBox="0 0 12 12"><path d="M1 2h10v8H1zm1.5 1.5v5h7v-5z"/><rect x="4" y="5" width="4" height="2"/></svg></span>Cartoon</li>
      <li><span class="mod-icon" style="background:var(--ic-grey)"><svg viewBox="0 0 12 12"><path d="M1 1h7v2H3v5H1z"/><path d="M4 4h7v7H4zm1.5 1.5v4h4v-4z"/></svg></span>Photo Album</li>
      <li><span class="mod-icon" style="background:var(--ic-grey)"><svg viewBox="0 0 12 12"><rect x="1" y="5" width="10" height="1.5"/><rect x="5" y="8" width="2" height="1.5"/></svg></span>Quotes</li>
      <li><span class="mod-icon" style="background:var(--ic-grey)"><svg viewBox="0 0 12 12"><path d="M2 9l5-5-1-1h4v4l-1-1-5 5z"/></svg></span>Follow</li>
    </ul>
  </section>

  <section class="col col-about">
    <h3 class="col-heading">
      <svg viewBox="0 0 24 24"><path d="M8 2h8v2h-1v5.5l6 10.5a2 2 0 0 1-1.7 3H4.7A2 2 0 0 1 3 20L9 9.5V4H8zm3 2v6l-2.4 4.2h6.8L13 10V4z"/></svg>
      About
    </h3>
    <ul class="link-list">
      <li>Introduction</li>
      <li>You &amp; Us</li>
      <li>Terms of Use</li>
      <li>Privacy Policy</li>
      <li>Contact</li>
    </ul>
  </section>

  <section class="col col-support">
    <h3 class="col-heading support">
      <svg viewBox="0 0 24 24"><path d="M2 10h4v12H2zm6 0l4-8c1.8 0 2.8 1.2 2.4 3L13.6 9H20a2 2 0 0 1 2 2.3l-1.5 8.7A2.5 2.5 0 0 1 18 22H8zm2 .5V20h8l1.5-8.5H11.2l1.3-5.4z"/></svg>
      Support
    </h3>
    <ul class="link-list support-list">
      <li>FAQ</li>
      <li>Contact us</li>
    </ul>
    <h3 class="col-heading legal">
      <svg viewBox="0 0 24 24"><path d="M10 2l8 8-3 3-2-2-9 9-3-3 9-9-2-2z"/><rect x="14" y="19" width="9" height="3"/></svg>
      Legal
    </h3>
    <ul class="link-list legal-list">
      <li>License</li>
      <li>Terms of Use</li>
      <li>Privacy Policy</li>
      <li>Security</li>
    </ul>
  </section>

  <section class="col col-contact">
    <h3 class="col-heading">Get in touch</h3>
    <div class="social-row first">
      <span>squawkr</span>
      <span>Chatterbox</span>
      <span>Linkmesh</span>
    </div>
    <div class="social-row second">
      <span>Orbitplus</span>
      <span>Codeden</span>
      <svg class="mail-icon" viewBox="0 0 32 24" aria-label="Email"><rect x="2" y="2" width="28" height="20" rx="1"/><path d="M2 3l14 11L30 3"/></svg>
    </div>
    <div class="phone">
      <svg viewBox="0 0 24 24"><path d="M6.6 2.5l3 3.6-2 2.3a14 14 0 0 0 7.9 7.9l2.3-2 3.6 3-1.9 3.2C11.5 20.5 3.5 12.5 3.5 4.4z"/></svg>
      +915550142233
    </div>
  </section>

  <section class="col col-newsletter">
    <h3 class="newsletter-heading">Get updated by email</h3>
    <div class="email-field">Email address</div>
    <div class="subscribe-btn">Subscribe</div>
  </section>

  <div class="footer-divider"></div>
  <p class="copyright">© 2013-2014 The Drifter Pass Website, Inc. All Rights Reserved.</p>
</footer>
</body>
</html>
```